Bref créative
Lark Meadow Stationary
Business Cards, Note Pads, Envelopes, Letterhead etc.
Professional
Doreen Vasquez
Executive Director
2718 North Tolliver Rd. Suite #416
Richardson, Texas 75093
dvasquez@larkmeadow-tx.com
www.larkmeadow-tx.com
Would like to see the card/stationary on cream or ivory colored card stock. Thanks
Lark Meadow Christian Outreach Ministries is the vehicle used to motivate women everywhere to recognize their potential and inner strength through Christ Jesus and use it to propel themselves and others into a new dimension of excellence. Using our talents and resources to build bridges not walls. Yielding a vessel worthy of the title WOMAN.

```html
<!DOCTYPE html>
<html lang="en">
<head>
<meta charset="utf-8">
<title>Lark Meadow Stationary – Business Card</title>
<link href="https://fonts.googleapis.com/css2?family=PT+Sans:wght@400;700&display=swap" rel="stylesheet">
<style>
  :root {
    --backdrop: #e6e4e1;
    --cream: #fbf6d6;
    --cream-edge: #f3ecc0;
    --gold: #c9962f;
    --gold-light: #e2bf6a;
    --brown: #6b4320;
    --brown-dark: #55331a;
    --text-light: #fbf3e0;
  }
  * { margin: 0; padding: 0; box-sizing: border-box; }
  html, body {
    width: 1200px;
    height: 928px;
    overflow: hidden;
    background: var(--backdrop);
    font-family: "PT Sans", Arial, sans-serif;
  }
  .business-card {
    position: absolute;
    left: 100px;
    top: 178px;
    width: 1000px;
    height: 571px;
    border-radius: 26px;
    overflow: hidden;
    background: var(--cream);
    box-shadow: 0 10px 30px rgba(0,0,0,0.18);
  }
  .card-shapes {
    position: absolute;
    inset: 0;
    width: 100%;
    height: 100%;
  }
  .identity {
    position: absolute;
    left: 60px;
    top: 230px;
    display: flex;
    align-items: center;
    gap: 20px;
  }
  .identity-dot {
    width: 104px;
    height: 104px;
    border-radius: 50%;
    background: var(--brown);
    flex: none;
  }
  .identity-name {
    color: var(--brown);
    font-weight: 700;
    font-size: 25px;
    line-height: 1.15;
    width: 240px;
  }
  .tagline {
    position: absolute;
    left: 60px;
    top: 366px;
    width: 360px;
    color: var(--brown);
    font-size: 13px;
    letter-spacing: 0.2px;
  }
  .person {
    position: absolute;
    left: 630px;
    right: 46px;
    top: 76px;
    color: var(--text-light);
  }
  .person-name {
    font-size: 44px;
    font-weight: 400;
    line-height: 1;
    white-space: nowrap;
  }
  .person-title {
    margin-top: 10px;
    font-size: 21px;
  }
  .contact {
    position: absolute;
    right: 46px;
    top: 250px;
    text-align: right;
    color: var(--text-light);
    font-size: 19px;
    line-height: 1.32;
  }
  .contact .gap { margin-top: 18px; }
  .contact b { font-weight: 700; }
</style>
</head>
<body>
  <div class="business-card">
    <svg class="card-shapes" viewBox="0 0 1000 571" preserveAspectRatio="none" aria-hidden="true">
      <path d="M520,0 C430,150 430,420 370,571 L1000,571 L1000,0 Z" fill="var(--gold-light)"/>
      <path d="M540,0 C450,150 450,420 390,571 L1000,571 L1000,0 Z" fill="var(--cream-edge)"/>
      <path d="M552,0 C462,150 462,420 402,571 L1000,571 L1000,0 Z" fill="var(--gold)"/>
      <path d="M580,0 C490,150 490,420 430,571 L1000,571 L1000,0 Z" fill="var(--brown)"/>
    </svg>

    <div class="identity">
      <span class="identity-dot"></span>
      <span class="identity-name">Lark Meadow Christian Outreach Ministries</span>
    </div>
    <p class="tagline">Using our talents and resources to build bridges not walls</p>

    <div class="person">
      <h1 class="person-name">Doreen Vasquez</h1>
      <p class="person-title">Executive Director</p>
    </div>

    <div class="contact">
      <p>2718 North Tolliver Rd.</p>
      <p>Suite #416</p>
      <p>Richardson, Texas 75093</p>
      <p class="gap"><b>P:</b> 214-555-0142</p>
      <p><b>F:</b> 214-555-0187</p>
      <p><b>E:</b> dvasquez@larkmeadow-tx.com</p>
      <p>www.larkmeadow-tx.com</p>
    </div>
  </div>
</body>
</html>
```